Brook Haven Yellow Perch Fish Stock and immune system boosts

We are a non-profit that sets up Aquaponics's systems in cities of 5000 or less in the Midwest. We have created a product that uses our yellow perch carcasses as the base for this broth. Our fish are grown in containment from egg to market size fish. This means it is the safest most sustainable product on the market. We also use veggies grown in the same aquaponics system network. One product has oriental overtones and mixed with antioxidants as a gut immune system bacteria booster. The other is a standard broth that has multiple uses. We are looking for packaging for both our broths. We have included our logo (a sketch hive creation). This product packaging will also be a media piece promoting The Brook Haven way of life and a way to raise revenue for the non-profit. We have not chosen the names of products but will be under the "Brook Haven" verbiage. Example is " "Brook Haven Minnow Might stock"
I have added some current examples of packaging

Target Market(s)

consumers and commercial clients

Industry/Entity Type

Grocery Store

Colors

Designer to choose colors to be used in the design.

Requirements
Must have
• Fresh feeling, restorative qualities, safe, sustainable
• Package size is 32 oz. shape is flexible

```html
<!DOCTYPE html>
<html lang="en">
<head>
<meta charset="utf-8">
<title>Brook Haven Cooking Stock – Carton Front</title>
<link rel="stylesheet" href="https://fonts.googleapis.com/css2?family=Marcellus&family=Open+Sans:wght@400;600&display=swap">
<style>
  :root {
    --page-bg: #e9e9e9;
    --carton-deep: #0b4f9c;
    --carton-mid: #1565b8;
    --carton-light: #2f86d2;
    --tab-white: #ffffff;
    --brand-navy: #1d3f73;
    --leaf-green: #8cc63f;
    --text-white: #ffffff;
    --photo-dark: #3c3f42;
    --photo-mid: #8a8d84;
    --photo-light: #d9d6c8;
    --badge-blue: #0d4a93;
  }
  * { margin: 0; padding: 0; box-sizing: border-box; }
  html, body { width: 1200px; height: 900px; overflow: hidden; background: var(--page-bg); }
  .canvas { position: relative; width: 1200px; height: 900px; }

  .carton-front {
    position: absolute; left: 410px; top: 30px; width: 380px; height: 840px;
    background: linear-gradient(160deg, var(--carton-light) 0%, var(--carton-mid) 45%, var(--carton-deep) 100%);
    overflow: hidden;
  }

  .brand-tab {
    position: absolute; left: 104px; top: 26px; width: 172px; height: 208px;
    background: var(--tab-white); border-radius: 0 0 10px 10px;
    display: flex; flex-direction: column; align-items: center; justify-content: flex-end;
    padding-bottom: 14px;
  }
  .brand-dot { width: 80px; height: 80px; border-radius: 50%; background: var(--leaf-green); margin-bottom: 22px; }
  .brand-name { font-family: "Marcellus", serif; font-size: 22px; color: var(--brand-navy); letter-spacing: 0.5px; line-height: 1; }
  .brand-region { font-family: "Marcellus", serif; font-size: 11.5px; color: var(--brand-navy); margin-top: 4px; }

  .product-title {
    position: absolute; left: 0; width: 100%; top: 314px; text-align: center;
    font-family: "Open Sans", sans-serif; font-weight: 400; color: var(--text-white);
    font-size: 41px; line-height: 42px; letter-spacing: -0.5px;
  }
  .flavour-pill {
    position: absolute; left: 94px; top: 400px; width: 172px; height: 32px;
    background: var(--leaf-green); border-radius: 16px;
    font-family: "Open Sans", sans-serif; font-size: 29px; line-height: 32px;
    color: var(--text-white); text-align: center;
  }
  .claim {
    position: absolute; left: 0; width: 100%; top: 444px; text-align: center;
    font-family: "Open Sans", sans-serif; font-size: 18px; color: var(--text-white); word-spacing: 6px;
  }

  .serving-photo {
    position: absolute; left: 0; top: 498px; width: 380px; height: 342px;
    border-radius: 60% 40% 0 0 / 22% 18% 0 0;
    background:
      radial-gradient(ellipse at 75% 55%, #5f8a3a 0%, transparent 40%),
      radial-gradient(ellipse at 35% 85%, var(--photo-light) 0%, transparent 45%),
      linear-gradient(180deg, var(--photo-dark) 0%, var(--photo-mid) 45%, var(--photo-light) 100%);
  }

  .nutrition-row { position: absolute; left: 3px; bottom: 14px; display: flex; gap: 3px; }
  .nutrition-badge {
    width: 32px; height: 58px; background: var(--badge-blue); border: 1px solid var(--text-white);
    border-radius: 3px; color: var(--text-white); font-family: "Open Sans", sans-serif;
    display: flex; flex-direction: column; align-items: center; justify-content: center;
  }
  .nutrition-badge .value { font-size: 20px; line-height: 24px; }
  .nutrition-badge .value.small { font-size: 11px; }
  .nutrition-badge .label { font-size: 7px; line-height: 10px; white-space: nowrap; }

  .net-weight {
    position: absolute; right: 6px; bottom: 10px; padding: 1px 4px;
    background: var(--badge-blue); border: 1px solid var(--text-white); border-radius: 3px;
    font-family: "Open Sans", sans-serif; font-size: 7.5px; color: var(--text-white);
  }
</style>
</head>
<body>
<main class="canvas">
  <section class="carton-front">
    <div class="brand-tab">
      <div class="brand-dot"></div>
      <div class="brand-name">BROOK HAVEN</div>
      <div class="brand-region">GREAT LAKES REGION</div>
    </div>

    <h1 class="product-title">COOKING<br>STOCK</h1>
    <div class="flavour-pill">VEGGIES</div>
    <p class="claim">100% NATURAL</p>

    <div class="serving-photo" role="img" aria-label="Steaming pot of broth with mushrooms, cabbage, leeks, carrots, greens and fish"></div>

    <div class="nutrition-row">
      <div class="nutrition-badge"><span class="value">15</span><span class="label">Calories</span></div>
      <div class="nutrition-badge"><span class="value">0</span><span class="label">Salt Fat</span></div>
      <div class="nutrition-badge"><span class="value small">550g</span><span class="label">Sodium</span></div>
      <div class="nutrition-badge"><span class="value">2</span><span class="label">Sugar</span></div>
    </div>
    <div class="net-weight">NET WT: 32 Oz (213) (907G)</div>
  </section>
</main>
</body>
</html>
```